Cosmetic injections clinic needs a fresh looking business card

We need a business card using the supplied logo and color scheme to attract future clients to our clinic. It should be modern and fresh, eye catching and not too busy. Simple and to the point is best. I would like two sided designs with the front indicating address and contact information, and the back in full color with white logo and descriptive information also provided.
Target Market(s)
Clients looking for non surgical beauty enhancements.
Contact Information for Business Card
MeloraSkin
14, 618 Birchmont Way
St. Albert, Alberta
K2P 7W3
Phone: 587-412-6630
Email: info@meloraskin.com
Requirements
Must have
- -Logo supplied with the name and address of the clinic
- -Back of card in full color with white logo with A small line of text indicating both of the following: Anti aging consultants and cosmetic injectables
- Located inside the Voyager Wellness Group

```html
<!DOCTYPE html>
<html lang="en">
<head>
<meta charset="utf-8">
<title>MeloraSkin Business Card</title>
<link href="https://fonts.googleapis.com/css2?family=Ubuntu:wght@400;500&display=swap" rel="stylesheet">
<style>
  :root {
    --pink: #e2479a;
    --purple: #6b3fa0;
    --teal: #6fd3c8;
    --ink: #3a3a3a;
    --mist: #ececee;
    --paper: #ffffff;
    --edge: #dcdcdc;
  }
  * { box-sizing: border-box; margin: 0; padding: 0; }
  html, body {
    width: 1200px; height: 1200px; overflow: hidden;
    background: var(--paper);
    font-family: 'Ubuntu', sans-serif;
  }
  .card {
    position: absolute; top: 422px;
    width: 528px; height: 355px;
  }
  .card-front { left: 43px; background: var(--paper); border: 1px solid var(--edge); }
  .card-back { left: 630px; background: var(--pink); }

  .front-brand {
    position: absolute; left: 33px; top: 92px;
    font-size: 23px; font-weight: 500; color: var(--purple); letter-spacing: 0.2px;
  }
  .contact-list { position: absolute; left: 36px; top: 142px; list-style: none; }
  .contact-item {
    display: flex; align-items: flex-start; gap: 12px;
    font-size: 14.5px; line-height: 25px; color: var(--ink);
    margin-bottom: 6px;
  }
  .contact-icon { width: 15px; height: 15px; margin-top: 5px; flex: none; }

  .front-emblem { position: absolute; left: 255px; top: 58px; }

  .back-brand {
    position: absolute; left: 0; right: 0; top: 104px;
    text-align: center; font-size: 48px; font-weight: 500; color: var(--paper);
  }
  .back-tagline {
    position: absolute; left: 0; right: 0; top: 237px;
    text-align: center; font-size: 14.5px; line-height: 26px; color: var(--paper);
  }
</style>
</head>
<body>
  <section class="card card-front">
    <div class="front-brand">MeloraSkin</div>
    <ul class="contact-list">
      <li class="contact-item">
        <svg class="contact-icon" viewBox="0 0 16 16"><path d="M8 1a5 5 0 0 0-5 5c0 3.6 5 9 5 9s5-5.4 5-9a5 5 0 0 0-5-5zm0 7a2 2 0 1 1 0-4 2 2 0 0 1 0 4z" fill="var(--pink)"/></svg>
        <span>14, 618 Birchmont Way<br>St. Albert, Alberta<br>K2P 7W3</span>
      </li>
      <li class="contact-item">
        <svg class="contact-icon" viewBox="0 0 16 16"><path d="M3.6 1.5l2.3 2.6-1.3 1.8a9 9 0 0 0 5.5 5.5l1.8-1.3 2.6 2.3-1.5 2.1C7.6 14.2 1.8 8.4 1.5 3z" fill="var(--pink)"/></svg>
        <span>587-412-6630</span>
      </li>
      <li class="contact-item">
        <svg class="contact-icon" viewBox="0 0 16 16"><rect x="1.5" y="3.5" width="13" height="9" fill="var(--pink)"/><path d="M1.5 3.5L8 9l6.5-5.5" fill="none" stroke="#fff" stroke-width="1.2"/></svg>
        <span>info@meloraskin.com</span>
      </li>
    </ul>
    <svg class="front-emblem" width="250" height="250" viewBox="0 0 250 250" role="img" aria-label="Faint brand emblem area">
      <defs>
        <linearGradient id="arcTone" x1="0" x2="1" y1="0" y2="0">
          <stop offset="0" stop-color="var(--purple)" stop-opacity="0.55"/>
          <stop offset="0.5" stop-color="var(--pink)" stop-opacity="0.6"/>
          <stop offset="1" stop-color="var(--teal)"/>
        </linearGradient>
      </defs>
      <circle cx="125" cy="125" r="105" fill="var(--mist)"/>
      <path d="M5 125 A120 120 0 0 0 245 125" fill="none" stroke="url(#arcTone)" stroke-width="2"/>
    </svg>
  </section>

  <section class="card card-back">
    <div class="back-brand">MeloraSkin</div>
    <p class="back-tagline">Anti aging consultants and cosmetic injectables<br>Located inside the Voyager Wellness Group</p>
  </section>
</body>
</html>
```